Web re-design project for web software development agency

We need to re-design our existing website (www.tovenmedia.co.uk), and are going to start using a shorter domain (www.toven.com).
We have been in business for 8 years and it's time for an update.

We are based at Harrowmede Court (home of the code breakers). We specialise in writing software for the web. Over the years we have built up a healthy customer base and it is time to incorporate the features we build for our customers into our own site (e.g. social media).

We have a team of 8 talented developers with varied skills including: apps for mobile; complex server side software; front-end software; eCommerce software; specialised web based applications; integration software; hardware support; consultancy services. Our customers are diverse (e.g. banking; commerce; veterinary; R&D; health sector; law; accounting; film industry etc.).

Our current colour scheme is blue, white and green although we are not averse to moving away from these colours. We will also be dropping the DESIGN from our name and logo. Revised logo will be attached.

The site needs to be modern, sophisticated and leading edge. We want to show visitors to the site that we are a professional organisation.
Updates

Our logo in PSD format has been uploaded. Please drop the word DESIGN from the logo.

The deliverable for this project is a PSD (ideally we would like to see how the home page, portfolio page, resources page with mugshots, and forms are going to look).

Many thanks,
Tom

Please DO NOT include a Careers section 

We will also need a "meet our team" section with spaces for 10 photographs as well as some space underneath them so that we can add a short paragraph for each one of them.

Target Market(s)

Mainly large corporations needing bespoke web software, or generally complex projects (for anyone).

Industry/Entity Type

Software

Requirements
Must have
• We would like a home page designed that has the following elements on it:
- Show the new cookie compliance policy displayed probably in the top of the page (will disappear).
- A client Testimonial.
- Pricing icon.
- Social media Links.
- A Quote section in expand/collapse field as in (http://www.quillbrook-online.co.uk/our-services.shtml)

We would also like a portfolio page that showcases our clients in an interesting way.

Finally, we would like a form design that we can use throughout the site (i.e. how should buttons, radio buttons, checkboxes, dropdowns, text areas etc. look)?
Nice to have
• A page that follows these guidelines:
http://www.pagerivet.com/the-anatomy-of-a-perfect-landing-page

Here are a few examples of sites in our sector that we like:
- http://www.tidewell-studio.com/
- http://plinthos.co.uk/
- http://www.fernaxis.com/services/web-development (nice contact us page)
- http://www.quillbrook-online.co.uk/
- http://www.lumsa.com/
- http://www.netmoxa.co.uk/
Should not have
• No flash elemets. If anything, we will use html5.

```html
<!DOCTYPE html>
<html lang="en">
<head>
<meta charset="utf-8">
<title>Toven – Internet Software Development</title>
<link rel="stylesheet" href="https://fonts.googleapis.com/css2?family=Open+Sans:ital,wght@0,400;0,600;0,700;1,400&family=Arimo:ital,wght@0,400;0,700;1,400&display=swap">
<style>
:root{
  --blue:#1b5f95;
  --navy:#0f3f6e;
  --band:#0d5a8f;
  --band-dark:#0a4b7c;
  --lime:#c5cf22;
  --ink:#222;
  --white:#fff;
  --grey:#f2f2f2;
}
*{box-sizing:border-box;margin:0;padding:0}
html,body{width:1059px;height:1200px;overflow:hidden;background:var(--white)}
body{position:relative;font-family:"Arimo",Arial,sans-serif;color:var(--ink)}
.abs{position:absolute}

.cookie-bar{left:0;top:0;width:1059px;height:34px;background:var(--band);border-top:3px solid var(--lime);color:var(--white);font-size:12.5px;font-weight:700}
.cookie-bar .msg{left:31px;top:9px}
.cookie-bar .hide{left:789px;top:6px;width:56px;height:22px;background:#1e2a55;text-align:center;line-height:22px;font-size:14px;letter-spacing:.5px}
.cookie-bar .what{left:860px;top:9px;font-weight:400}

.call{right:34px;top:41px;font-size:16px;font-weight:700;color:#222}
.call span{color:var(--blue);font-size:18px;font-weight:400;margin-left:3px}

.brand{left:35px;top:58px;display:flex;align-items:center;gap:8px}
.brand .mark{width:38px;height:38px;background:var(--lime)}
.brand .name{font-family:"Arimo",Arial,sans-serif;font-weight:700;font-size:40px;color:var(--blue);letter-spacing:1px;line-height:1}

.nav{left:305px;top:81px;display:flex;gap:0;font-size:13.5px;font-weight:700;color:var(--navy)}
.nav a{padding:3px 5px;margin-right:13px;color:inherit;text-decoration:none}
.nav a.active{background:var(--lime);color:#1a1a4a}

.hero{left:20px;top:128px;width:1019px;height:284px;background:linear-gradient(90deg,#1a6ea8,#0f5a94 55%,#0c4e86);border-radius:3px 3px 0 0;border-bottom:4px solid var(--lime)}
.hero .showcase{left:38px;top:6px;width:590px;height:270px;background:linear-gradient(180deg,#2b79b0 0%,#e9eef2 30%,#cfdbe6 70%,#1b6aa5 100%);border-radius:4px;opacity:.9}
.hero .title{left:646px;top:90px;color:var(--white);font-family:"Open Sans",sans-serif;font-weight:600;font-size:30px}
.hero .sub{left:651px;top:137px;color:var(--white);font-weight:700;font-size:21px;line-height:26px;text-transform:uppercase}
.quote-btn{left:795px;top:245px;width:187px;height:37px;background:linear-gradient(#d5dc3b,var(--lime));text-align:center;line-height:37px;font-family:"Open Sans",sans-serif;font-size:19px;color:#333;border-radius:2px 2px 0 0}

.intro h1{font-family:"Open Sans",sans-serif;font-weight:600;font-size:24px;color:var(--blue);position:absolute;left:30px;top:432px;white-space:nowrap}
.intro p{position:absolute;left:31px;top:466px;width:650px;font-family:"Open Sans",sans-serif;font-size:17.5px;line-height:25px;color:#222}

.can-box{left:33px;top:536px;width:615px;height:209px;background:linear-gradient(180deg,#f6f6f6,#e2e2e2 55%,#f3f3f3);border:1px solid #cfcfcf;border-radius:5px;box-shadow:0 6px 8px -4px rgba(0,0,0,.18)}
.can-tab{left:28px;top:552px;width:160px;height:35px;background:var(--blue);color:var(--white);font-family:"Open Sans",sans-serif;font-size:19px;line-height:35px;padding-left:16px;clip-path:polygon(0 0,90% 0,100% 100%,0 100%)}
.can-list{left:114px;top:609px;list-style:none;font-family:"Open Sans",sans-serif;font-size:15px;font-weight:600;color:#1f1f1f}
.can-list li{height:31.5px;display:flex;align-items:center;gap:8px}

.trusted{left:34px;top:775px;font-family:"Open Sans",sans-serif;font-size:18px;font-weight:600;color:var(--blue)}
.client{height:38px;border:1px solid #c7c7c7;background:#fafafa;box-shadow:1px 1px 2px rgba(0,0,0,.25);display:flex;align-items:center;justify-content:center;font-family:"Arimo",sans-serif;font-weight:700;font-size:13px;color:var(--blue)}

.side h2{position:absolute;font-family:"Open Sans",sans-serif;font-weight:600;font-size:20px;color:var(--blue)}
.services{left:728px;top:466px;list-style:none;font-size:14.5px;color:#222}
.services li{height:25.5px;display:flex;align-items:center}
.services li::before{content:"";width:6px;height:6px;border-radius:50%;background:#444;margin:0 12px 0 2px}
.testimonial{left:728px;top:731px;width:269px;font-style:italic;font-size:13.5px;line-height:25.5px;text-align:justify;color:#222}
.cite{left:738px;top:896px;font-size:14px;font-weight:700;color:#222}

.footer{left:0;top:940px;width:1059px;height:260px;background:var(--band);border-top:4px solid var(--lime);color:var(--white)}
.footer h3{position:absolute;font-size:13.5px;font-weight:700;top:25px}
.footer ul{position:absolute;list-style:none;top:46px;font-size:12.5px;line-height:19px}
.social{top:50px;width:55px;height:58px;border-radius:8px;background:linear-gradient(#eaf3fb,#b9d3e8);color:var(--blue);font-size:9.5px;font-weight:700;display:flex;align-items:center;justify-content:center}
.company{left:751px;top:22px;font-size:13.5px;line-height:17px}
.company .contact{display:grid;grid-template-columns:63px auto;margin-top:7px;font-weight:700}
.company .contact span:nth-child(even){font-weight:400}
.bottom-bar{left:0;top:1156px;width:1059px;height:44px;background:var(--band-dark);border-top:4px solid var(--lime)}
.share{left:37px;top:1158px;width:92px;height:29px;background:var(--lime);color:#1a3a5a;font-family:"Open Sans",sans-serif;font-size:17px;font-weight:600;display:flex;align-items:center;justify-content:center;gap:7px}
.copyright{right:97px;top:1175px;color:var(--white);font-size:11px}
</style>
</head>
<body>

<div class="abs cookie-bar">
  <span class="abs msg">We'd like to set optional cookies to make your user experience better, by using this site you give your consent for us to do this.</span>
  <span class="abs hide">HIDE</span>
  <span class="abs what">What are cookies?</span>
</div>

<div class="abs call">CALL US <span>01632 960 418</span></div>

<div class="abs brand">
  <div class="mark"></div>
  <div class="name">TOVEN</div>
</div>

<nav class="abs nav">
  <a class="active">HOME</a><a>ABOUT US</a><a>OUR SERVICES</a><a>TECHNOLOGY</a><a>PORTFOLIO</a><a>MEET OUR TEAM</a><a>CONTACT US</a>
</nav>

<section class="abs hero">
  <div class="abs showcase" role="img" aria-label="Consultant standing beside a row of client website screenshots"></div>
  <div class="abs title">We specialise in</div>
  <div class="abs sub">Web application development<br>and support</div>
  <div class="abs quote-btn">Get a Quote</div>
</section>

<section class="intro">
  <h1>We are an Internet Software Development Company</h1>
  <p>Our passion is developing complex applications for the web that work for you and your business.</p>
</section>

<div class="abs can-box"></div>
<div class="abs can-tab">We can</div>
<ul class="abs can-list">
  <li><svg width="17" height="15" viewBox="0 0 17 15"><path d="M1 8l5 5L16 1" fill="none" stroke="#222" stroke-width="3"/></svg>turn your business processes into online web applications.</li>
  <li><svg width="17" height="15" viewBox="0 0 17 15"><path d="M1 8l5 5L16 1" fill="none" stroke="#222" stroke-width="3"/></svg>get your products or services selling online.</li>
  <li><svg width="17" height="15" viewBox="0 0 17 15"><path d="M1 8l5 5L16 1" fill="none" stroke="#222" stroke-width="3"/></svg>convert your site into one that you can maintain yourself.</li>
  <li><svg width="17" height="15" viewBox="0 0 17 15"><path d="M1 8l5 5L16 1" fill="none" stroke="#222" stroke-width="3"/></svg>help ensure your website is usable and standards compliant.</li>
</ul>

<div class="abs trusted">Trusted by thousands of businesses</div>
<div class="abs client" style="left:37px;top:817px;width:126px">Aurelvault</div>
<div class="abs client" style="left:193px;top:819px;width:100px">Ledgerline</div>
<div class="abs client" style="left:322px;top:817px;width:100px">Lumora Labs</div>
<div class="abs client" style="left:449px;top:813px;width:98px;height:57px">Pitchside Sites</div>
<div class="abs client" style="left:37px;top:874px;width:121px;height:34px">Rattlebox Audio</div>
<div class="abs client" style="left:178px;top:881px;width:124px;height:32px">Veterna</div>
<div class="abs client" style="left:322px;top:871px;width:66px;height:44px">Lucidar</div>

<aside class="side">
  <h2 style="left:726px;top:432px">Featured Services</h2>
  <ul class="abs services">
    <li>Apps development for mobile</li>
    <li>Complex server side software</li>
    <li>Front-end software;</li>
    <li>eCommerce software</li>
    <li>Specialised web based applications</li>
    <li>Integration software</li>
    <li>Hardware support</li>
    <li>Consultancy services</li>
  </ul>
  <h2 style="left:728px;top:697px">What clients are saying</h2>
  <p class="abs testimonial">“Lorem ipsum dolor sit amet, ea facilisi recteque eos, has no graece deserunt. Eu maiorum fastidii albucius nec, vix ea nisl aliquip expetenda. Vim in inani feugiat incor-rupte, utamur nominati delicata mel in, usu te quaeque repudiare definitiones.”</p>
  <div class="abs cite">- ABC</div>
</aside>

<footer class="abs footer">
  <h3 style="left:33px">OUR SERVICES</h3>
  <ul style="left:37px">
    <li>Apps development for mobile</li><li>Complex server side software</li><li>Front-end software;</li><li>eCommerce software</li><li>Specialised web based applications</li><li>Integration software</li><li>Hardware support</li><li>Consultancy services</li>
  </ul>
  <h3 style="left:283px">TECHNOLOGY</h3>
  <ul style="left:287px">
    <li>The Solanix operating system</li><li>Pixelforge and Vectorist</li><li>Hardware Installation and Support</li><li>Software Installation and Support</li><li>HTML,XML, CSS, PHP, Javascript,</li><li>DataQL, Ajax, QueryKit</li>
  </ul>
  <h3 style="left:561px;font-size:12.5px">FOLLOW US</h3>
  <div class="abs social" style="left:558px">Chirpline</div>
  <div class="abs social" style="left:621px">Facepage</div>
  <div class="abs company">
    <strong>TOVEN&nbsp; LTD</strong><br>
    <div style="margin-top:5px">Suite B2/5, Venture and Research Centre,<br>Harrowmede Court, Harrowmede HM3 6QX</div>
    <div class="contact"><span>Tel:</span><span>01632 960 418</span><span>Email:</span><span>info@toven.co.uk</span></div>
  </div>
</footer>
<div class="abs bottom-bar"></div>
<div class="abs share">Share <svg width="8" height="10" viewBox="0 0 8 10"><path d="M0 0l8 5-8 5z" fill="#1a3a5a"/></svg></div>
<div class="abs copyright">Copyright 2012 Toven</div>

</body>
</html>
```